NEW Modern Sleek Business Card for VR Language Startup

Our startup is using VR to lead the next wave of world language education. We need a two-sided business card that introduces the larger organization (Quorvel Language Inc) and our contact info on one side and shows the product, Lumidrasca, on the other side.

Side 1 (contact info)= Quorvel Logo and Contact info (name, title, phone, email)

Side 2 (product)= Lumidrasc logo, text, and website
Text= Culturally Immersive Language Learning Games
Website= www.lumidrasc.example

Target Market(s)

Education, Technology

Contact Information for Business Card

Contact info will be updated upon approval of the design. For now, put this as a placeholder.

Perry Hollins
Founder & CEO
phollins@mailtrove.example
(555)-014-2736

Font styles to use
Other font styles liked:
• Gibson and Century Gothic are the brand fonts

Requirements
Nice to have
• I would love to see cohesion between the design and colors of the two logos. I have attached a few business card designs that I like, so you can get a feel for my preferred style.

```html
<!DOCTYPE html>
<html lang="en">
<head>
<meta charset="utf-8">
<title>Quorvel Language – Business Card</title>
<link rel="stylesheet" href="https://fonts.googleapis.com/css2?family=Hind:wght@400;500;600;700&family=Questrial&display=swap">
<style>
  :root {
    --stage: #343a46;
    --paper: #ffffff;
    --card-dark: #242122;
    --ink: #2b2b2e;
    --ink-soft: #6b6b70;
    --orange: #f39a2e;
    --coral: #ec5a4a;
    --magenta: #c94e96;
    --violet: #7c5cc6;
    --sky: #3fa9e6;
    --bar: #8a63c9;
    --light: #f2f2f2;
    --muted: #cfcfd2;
  }
  * { box-sizing: border-box; margin: 0; padding: 0; }
  html, body { width: 1200px; height: 900px; overflow: hidden; }
  body {
    background: var(--stage);
    font-family: "Hind", "Helvetica Neue", Arial, sans-serif;
    position: relative;
  }
  .card {
    position: absolute;
    left: 285px;
    width: 630px;
    height: 364px;
    overflow: hidden;
  }
  .card--front { top: 35px; background: var(--paper); }
  .card--back  { top: 464px; background: var(--card-dark); }

  .front-wave { position: absolute; inset: 0; width: 100%; height: 100%; }

  .brand {
    position: absolute;
    left: 44px;
    top: 54px;
    display: flex;
    align-items: center;
    gap: 16px;
  }
  .brand__dot {
    width: 72px; height: 72px; border-radius: 50%;
    background: linear-gradient(160deg, var(--coral), var(--magenta) 50%, var(--sky));
  }
  .brand__name {
    font-family: "Questrial", "Century Gothic", sans-serif;
    font-size: 34px;
    letter-spacing: 3px;
    color: var(--ink);
    line-height: 1.05;
    width: 200px;
  }

  .contact {
    position: absolute;
    right: 52px;
    top: 198px;
    text-align: right;
    color: #fff;
  }
  .contact__name { font-size: 20px; font-weight: 700; line-height: 1.1; }
  .contact__title { font-size: 15px; font-weight: 400; line-height: 1.3; margin-right: 0; }
  .contact__list { list-style: none; margin-top: 26px; }
  .contact__item {
    display: flex; justify-content: flex-end; align-items: center;
    gap: 8px; font-size: 15px; line-height: 19px;
  }
  .contact__icon { width: 15px; height: 15px; flex: none; }

  .product-mark {
    position: absolute;
    left: 98px;
    top: 106px;
    width: 190px;
    text-align: center;
  }
  .product-mark__dot {
    width: 86px; height: 86px; border-radius: 50%;
    margin: 0 auto 22px;
    background: linear-gradient(160deg, var(--sky), var(--violet));
  }
  .product-mark__name {
    font-size: 34px; font-weight: 500; color: var(--sky); line-height: 1;
  }

  .tagline {
    position: absolute;
    left: 328px;
    top: 124px;
    color: var(--light);
  }
  .tagline__lead, .tagline__tail { font-size: 16px; line-height: 22px; }
  .tagline__key { font-size: 20px; font-weight: 700; color: var(--sky); line-height: 26px; }
  .tagline__rule {
    width: 27px; height: 3px; background: var(--bar);
    margin: 16px 0 12px;
  }
  .tagline__web {
    font-family: "Questrial", "Century Gothic", sans-serif;
    font-size: 14px; letter-spacing: 1.5px; color: var(--light);
  }
  .tagline__web span { color: var(--sky); }
</style>
</head>
<body>

<section class="card card--front" aria-label="Business card, contact side">
  <svg class="front-wave" viewBox="0 0 700 404" preserveAspectRatio="none" aria-hidden="true">
    <defs>
      <linearGradient id="waveFill" x1="0.9" y1="0" x2="0.6" y2="1">
        <stop offset="0" stop-color="#f39a2e"/>
        <stop offset="0.25" stop-color="#ec5a4a"/>
        <stop offset="0.5" stop-color="#c94e96"/>
        <stop offset="0.78" stop-color="#7c5cc6"/>
        <stop offset="1" stop-color="#3fa9e6"/>
      </linearGradient>
    </defs>
    <path d="M272,404 C248,318 300,232 424,194 L442,199 C322,238 266,320 292,404 Z" fill="#ec5a3a"/>
    <path d="M480,0 H700 V404 H292 C266,320 322,238 442,199 C540,168 600,130 626,52 C588,118 548,140 572,94 C596,48 562,14 480,0 Z" fill="url(#waveFill)"/>
    <path d="M488,0 C566,16 590,52 574,94" fill="none" stroke="#7c5cc6" stroke-width="4"/>
  </svg>

  <div class="brand">
    <div class="brand__dot"></div>
    <div class="brand__name">Quorvel Language</div>
  </div>

  <div class="contact">
    <p class="contact__name">Perry Hollins</p>
    <p class="contact__title">Founder &amp; CEO</p>
    <ul class="contact__list">
      <li class="contact__item">555.014.2736
        <svg class="contact__icon" viewBox="0 0 16 16" aria-hidden="true"><circle cx="8" cy="8" r="7.5" fill="#fff"/><path d="M5.2 4.3l1.3-.3.8 2-.9.7a5 5 0 0 0 2.9 2.9l.7-.9 2 .8-.3 1.3c-3.8.2-6.7-2.7-6.5-6.5z" fill="#8a63c9"/></svg>
      </li>
      <li class="contact__item">phollins@mailtrove.example
        <svg class="contact__icon" viewBox="0 0 16 16" aria-hidden="true"><circle cx="8" cy="8" r="7.5" fill="#fff"/><rect x="4" y="5.3" width="8" height="5.6" fill="none" stroke="#7c5cc6" stroke-width="1"/><path d="M4 5.3l4 3 4-3" fill="none" stroke="#7c5cc6" stroke-width="1"/></svg>
      </li>
      <li class="contact__item">www.perryhollins.example
        <svg class="contact__icon" viewBox="0 0 16 16" aria-hidden="true"><circle cx="8" cy="8" r="7.5" fill="#fff"/><circle cx="8" cy="8" r="4" fill="none" stroke="#6d6fd0" stroke-width="1"/><path d="M4 8h8M8 4c-2 2.5-2 5.5 0 8M8 4c2 2.5 2 5.5 0 8" fill="none" stroke="#6d6fd0" stroke-width="0.9"/></svg>
      </li>
    </ul>
  </div>
</section>

<section class="card card--back" aria-label="Business card, product side">
  <div class="product-mark">
    <div class="product-mark__dot"></div>
    <p class="product-mark__name">Lumidrasc</p>
  </div>

  <div class="tagline">
    <p class="tagline__lead">Culturally</p>
    <p class="tagline__key">IMMERSIVE Language</p>
    <p class="tagline__tail">Learning Games</p>
    <div class="tagline__rule"></div>
    <p class="tagline__web">www.<span>lumidrasc</span>.example</p>
  </div>
</section>

</body>
</html>
```